Torvel & Company: Business Cards, Stationery & Envelopes
Our Tagline is "Speak Up."
Simple
Marla Drosset
Founder, Torvel & Company
217 Meadow Lantern Dr.
Briar Glen, North Carolina 27584
2816 Halloway Brook, NE
Harlow Springs, Georgia 30361
Marla@TorvelAndCo.example
www.TorvelAndCo.example
My consulting firm helps CEOs and other high-level executives with high-stakes communications. Our materials must exude professionalism and a modern, fresh, crisp and clean feel. The business cards, stationery and envelopes should match the look and feel of the logo and website. I'm interested in seeing designs that incorporate our "Be Heard" tagline, as well as ones that don't.
I think I prefer a card that is single-sided, but if you think there's a cool design that puts some information such as our addresses on back, I'm open to it.
Here are the relevant logo files

```html
<!DOCTYPE html>
<html lang="en">
<head>
<meta charset="utf-8">
<title>Torvel &amp; Company — Business Cards</title>
<link rel="stylesheet" href="https://fonts.googleapis.com/css2?family=Arimo:wght@400;700&display=swap">
<style>
  :root {
    --backdrop: #e9e6e2;
    --card-white: #ffffff;
    --card-grey: #e4e4e4;
    --brand-red: #d5121b;
    --brand-red-bright: #f0161f;
    --brand-dark: #2a0a0c;
    --ink: #2b2b2b;
    --ink-soft: #555555;
    --shadow: rgba(0, 0, 0, 0.28);
  }
  html, body {
    margin: 0;
    padding: 0;
    width: 1200px;
    height: 911px;
    overflow: hidden;
    background: var(--backdrop);
    font-family: "Arimo", Arial, sans-serif;
  }
  .stage {
    position: relative;
    width: 1200px;
    height: 911px;
  }
  .card {
    position: absolute;
    width: 420px;
    height: 237px;
    border-radius: 12px;
    overflow: hidden;
    box-shadow: 4px 8px 18px var(--shadow);
  }

  /* Front of card */
  .card-front {
    left: 143px;
    top: 304px;
    z-index: 3;
    background: linear-gradient(180deg, var(--card-white) 0%, #f7f7f7 55%, var(--card-grey) 100%);
  }
  .brand {
    position: absolute;
    left: 26px;
    top: 24px;
    display: flex;
    align-items: center;
    gap: 10px;
  }
  .brand-dot {
    width: 30px;
    height: 30px;
    border-radius: 50%;
    background: var(--brand-red);
  }
  .brand-name {
    font-size: 22px;
    font-weight: 700;
    color: var(--ink);
    letter-spacing: 0.5px;
  }
  .tagline {
    position: absolute;
    left: 206px;
    top: 53px;
    font-size: 10px;
    font-weight: 700;
    color: var(--brand-red);
  }
  .contact {
    position: absolute;
    left: 70px;
    top: 78px;
    color: var(--ink-soft);
    font-size: 8.5px;
    line-height: 12px;
  }
  .contact-name {
    font-size: 15px;
    font-weight: 700;
    line-height: 18px;
    color: var(--brand-red);
  }
  .contact-title { margin-bottom: 12px; }
  .contact-block { margin-bottom: 8px; }
  .front-band {
    position: absolute;
    left: 0;
    right: 0;
    bottom: 0;
    height: 22px;
    background: linear-gradient(90deg, var(--brand-red-bright) 0%, var(--brand-red) 45%, var(--brand-dark) 100%);
  }
  .front-band .url {
    position: absolute;
    right: 18px;
    top: 6px;
    font-size: 9px;
    font-weight: 700;
    color: var(--card-white);
  }

  /* Red back */
  .card-back-red {
    left: 630px;
    top: 210px;
    z-index: 1;
    background: linear-gradient(90deg, var(--brand-red-bright) 0%, var(--brand-red) 45%, #7a0a10 78%, var(--brand-dark) 100%);
  }
  .back-glow {
    position: absolute;
    right: 30px;
    top: 30px;
    width: 200px;
    height: 180px;
    border-radius: 50%;
    background: radial-gradient(circle, rgba(255,255,255,0.08) 0%, rgba(255,255,255,0) 70%);
  }
  .back-mark {
    position: absolute;
    left: 22px;
    bottom: 22px;
  }
  .back-mark .mark-name {
    font-size: 11px;
    font-weight: 700;
    color: var(--card-white);
  }
  .back-mark .url {
    margin-top: 4px;
    font-size: 7.5px;
    color: var(--card-white);
  }

  /* White back */
  .card-back-white {
    left: 365px;
    top: 511px;
    z-index: 2;
    background: linear-gradient(180deg, var(--card-white) 0%, #f6f6f6 60%, var(--card-grey) 100%);
  }
  .card-back-white .back-glow {
    background: radial-gradient(circle, rgba(213,18,27,0.10) 0%, rgba(213,18,27,0) 70%);
  }
  .card-back-white .mark-name { color: var(--brand-red); }
  .card-back-white .url { color: var(--ink-soft); }
</style>
</head>
<body>
<main class="stage">

  <section class="card card-front" aria-label="Business card front">
    <div class="brand">
      <span class="brand-dot"></span>
      <span class="brand-name">Torvel &amp; Company</span>
    </div>
    <div class="tagline">Speak Up.</div>
    <div class="contact">
      <div class="contact-name">Marla Drosset</div>
      <div class="contact-title">Founder, Torvel &amp; Company</div>
      <div class="contact-block">217 Meadow Lantern Dr.<br>Briar Glen, North Carolina 27584</div>
      <div>2816 Halloway Brook, NE<br>Harlow Springs, Georgia 30361<br>Cell: 555 210 0172<br>Email: Marla@TorvelAndCo.example</div>
    </div>
    <div class="front-band"><span class="url">www.TorvelAndCo.example</span></div>
  </section>

  <section class="card card-back-red" aria-label="Business card back, red">
    <div class="back-glow"></div>
    <div class="back-mark">
      <div class="mark-name">Torvel &amp; Company</div>
      <div class="url">www.TorvelAndCo.example</div>
    </div>
  </section>

  <section class="card card-back-white" aria-label="Business card back, white">
    <div class="back-glow"></div>
    <div class="back-mark">
      <div class="mark-name">Torvel &amp; Company</div>
      <div class="url">www.TorvelAndCo.example</div>
    </div>
  </section>

</main>
</body>
</html>
```